Urkundendesign für Jahrgangsbeste einer Realschule gesucht
Der Elternbeirat der Realschule Lindwerth benötigt für die Jahrgangsbesten des Abschlussjahrgangs eine Urkunde. Gerne mit Prägung (was kostet sowas bei Druck?!?). Das von-Halmberg-Logo darf benutzt werden (siehe Homepage).
es soll eine Urkunde für den/die 'Jahrgangsbeste 2026' geben. das Datum, sowie SchülerInnen-Name würden wir jeweils handschriftlich anbringen.
die Urkunde in A4 gestalten.
wir benötigen die üblichen druckbaren Dateien, sodass eine Druckerei dann auch selbst Jahr für Jahr das Jahr abändern kann.
bitte um Vorschläge, wir arbeiten uns nach und nach da durch.
nicht zu viel Schnörkelei.

```html
<!DOCTYPE html>
<html lang="de">
<head>
<meta charset="utf-8">
<title>Urkunde Jahrgangsbeste – Realschule Lindwerth</title>
<link rel="stylesheet" href="https://fonts.googleapis.com/css2?family=Lexend:wght@300;400&family=Great+Vibes&family=Mrs+Saint+Delafield&family=Cormorant+Garamond:ital,wght@1,400&display=swap">
<style>
  :root {
    --paper: #ffffff;
    --ink: #2b2b2b;
    --ink-soft: #4a4a4a;
    --green-dark: #1f8f4e;
    --green-mid: #3fae49;
    --green-light: #86d923;
    --accent-red: #c8242c;
    --accent-yellow: #f2c11a;
    --rule: #555555;
  }
  * { margin: 0; padding: 0; box-sizing: border-box; }
  html, body { width: 848px; height: 1200px; overflow: hidden; background: var(--paper); }
  .certificate { position: relative; width: 848px; height: 1200px; background: var(--paper); color: var(--ink); font-family: "Lexend", sans-serif; }
  .frame-art { position: absolute; inset: 0; }
  .content { position: absolute; left: 0; top: 0; width: 750px; text-align: center; }
  .school-mark { position: absolute; left: 335px; top: 175px; width: 80px; height: 80px; border-radius: 50%; background: var(--green-mid); }
  .school-name { position: absolute; top: 282px; width: 750px; font-size: 30px; font-weight: 400; color: var(--ink-soft); }
  .intro { position: absolute; top: 345px; width: 750px; font-size: 17px; font-weight: 300; }
  .title { position: absolute; top: 395px; width: 750px; font-family: "Great Vibes", cursive; font-size: 104px; line-height: 1; }
  .reason { position: absolute; top: 520px; width: 750px; font-size: 19px; font-weight: 300; }
  .word-an, .word-als, .year-label { position: absolute; width: 750px; font-size: 16px; font-weight: 300; }
  .word-an { top: 552px; }
  .recipient { position: absolute; top: 585px; left: 215px; width: 320px; font-family: "Mrs Saint Delafield", cursive; font-size: 66px; line-height: 1; border-bottom: 2px solid var(--ink); text-align: center; padding-bottom: 4px; }
  .word-als { top: 735px; }
  .award { position: absolute; top: 775px; width: 750px; font-family: "Great Vibes", cursive; font-size: 58px; line-height: 1; }
  .year-label { top: 860px; }
  .school-year { position: absolute; top: 890px; width: 750px; font-family: "Cormorant Garamond", serif; font-style: italic; font-size: 56px; letter-spacing: 3px; }
  .signature { position: absolute; left: 48px; top: 1120px; width: 250px; border-top: 1px solid var(--rule); padding-top: 4px; font-size: 11px; font-weight: 300; color: var(--ink-soft); }
</style>
</head>
<body>
<main class="certificate">
  <svg class="frame-art" width="848" height="1200" viewBox="0 0 848 1200" aria-hidden="true">
    <defs>
      <linearGradient id="band-fill" x1="0" y1="0" x2="1" y2="0">
        <stop offset="0" stop-color="var(--green-dark)"/>
        <stop offset="0.75" stop-color="var(--green-light)"/>
        <stop offset="1" stop-color="var(--green-mid)"/>
      </linearGradient>
      <linearGradient id="panel-fill" x1="0" y1="0" x2="0.3" y2="1">
        <stop offset="0" stop-color="var(--green-dark)"/>
        <stop offset="0.5" stop-color="var(--green-mid)"/>
        <stop offset="1" stop-color="var(--green-light)"/>
      </linearGradient>
    </defs>
    <polygon class="top-band" points="0,0 848,0 848,150 0,82" fill="url(#band-fill)"/>
    <line class="top-rule" x1="0" y1="88" x2="848" y2="156" stroke="var(--accent-red)" stroke-width="4"/>
    <polygon class="side-panel" points="640,158 848,168 848,1135 815,1135" fill="url(#panel-fill)"/>
    <polygon class="side-panel-facet" points="760,400 848,380 848,700" fill="#ffffff" opacity="0.12"/>
    <polygon class="side-panel-facet" points="790,820 848,760 848,1000" fill="#0d6b35" opacity="0.25"/>
    <line class="side-rule" x1="640" y1="158" x2="815" y2="1135" stroke="var(--accent-yellow)" stroke-width="4"/>
  </svg>

  <section class="content">
    <div class="school-mark" aria-hidden="true"></div>
    <p class="school-name">Realschule Lindwerth</p>
    <p class="intro">In Anerkennung verleihen wir diese</p>
    <h1 class="title">Urkunde</h1>
    <p class="reason">für herausragende schulische Leistungen</p>
    <p class="word-an">an</p>
    <p class="recipient">Lena Beispielfrau</p>
    <p class="word-als">als</p>
    <p class="award">Jahrgangsbeste/r</p>
    <p class="year-label">im Schuljahr</p>
    <p class="school-year">2025/2026</p>
  </section>

  <p class="signature">Datum, Unterschrift</p>
</main>
</body>
</html>
```